Wordpress Web Design Project for Upmarket Trendy Modern Travel Agency

We are a independent travel agency that does not offer online bookings (at this stage). We offer quality service and this needs to be reflected somehow in the design i.e. good old fashioned service.

Looking for wordpress Design for Travel Site

Company Name Voyage Harbour

www.voyageharbour-example.com.au

Looking for something outside the box and not from layout lagoon.

Something uniquely different !

Reason: Just have not see the right design.

Target Market(s)

Everyone

Industry/Entity Type

Travel

Requirements
Must have
• 1. Booking form
2. Seo friendly layout
3. Everything should be managed from wordpress admin

```html
<!DOCTYPE html>
<html lang="en">
<head>
<meta charset="utf-8">
<title>Voyage Harbour – Travel Agency</title>
<link rel="stylesheet" href="https://fonts.googleapis.com/css2?family=Arimo:wght@400;700&family=Roboto+Condensed:wght@400;700&family=Playfair+Display:wght@400;700&display=swap">
<style>
:root{
  --blue:#1d5a8e;
  --blue-dark:#174a76;
  --navy:#1b4f7d;
  --yellow:#fcc40f;
  --yellow-soft:#ffd43a;
  --ink:#333;
  --muted:#555;
  --line:#dcdcdc;
  --grey-bg:#eeeeec;
  --white:#fff;
  --body:"Arimo", Arial, sans-serif;
  --cond:"Roboto Condensed", Arial, sans-serif;
  --serif:"Playfair Display", Georgia, serif;
}
*{box-sizing:border-box;margin:0;padding:0}
html,body{width:1102px;height:1200px;overflow:hidden;background:var(--white);font-family:var(--body);color:var(--ink)}
.page{position:relative;width:1102px;height:1200px;overflow:hidden}
.abs{position:absolute}

/* header */
.site-header{left:0;top:0;width:1102px;height:55px;background:linear-gradient(#fff,#f1f1f1)}
.brand{left:207px;top:14px;font-family:var(--body);font-size:18px;letter-spacing:1.5px;color:var(--blue)}
.brand .sub{display:block;font-size:6px;letter-spacing:2px;text-align:right;margin-top:1px}
.search{left:454px;top:15px;width:219px;height:23px;border:1px solid #cfcfcf;background:#fff;display:flex}
.search span{flex:1;font-size:8px;color:#999;padding:6px 8px}
.search .go{width:22px;background:#222;display:flex;align-items:center;justify-content:center}
.call{left:702px;top:17px;display:flex;align-items:center;gap:4px}
.call .label{font-size:11px;color:#222}
.call .num{font-family:var(--cond);font-size:17px;color:var(--yellow)}

/* nav */
.main-nav{left:0;top:55px;width:1102px;height:41px;background:var(--blue)}
.main-nav ul{list-style:none;position:absolute;left:208px;top:14px;display:flex}
.main-nav li{font-family:var(--cond);font-size:11px;color:#fff;padding:0 7px;border-left:1px dotted #6f9cc6}
.main-nav li:first-child{padding-left:0;border:none}
.newsletter{left:697px;top:55px;width:405px;height:41px;background:var(--yellow);clip-path:polygon(18px 0,100% 0,100% 100%,18px 100%,0 50%)}
.newsletter span{position:absolute;left:29px;top:10px;font-family:var(--serif);font-size:16px;color:#222}

/* hero */
.hero{left:0;top:96px;width:1102px;height:343px;background:linear-gradient(180deg,#5fb9ea 0%,#a9dcf5 55%,#e7f4fb 100%)}
.hero-title{left:294px;top:350px;width:546px;color:#111}
.hero-title .welcome{position:absolute;left:0;top:32px;font-family:var(--cond);font-size:17px;letter-spacing:-.5px}
.hero-title .name{position:absolute;left:106px;top:0;font-family:var(--serif);font-size:48px;letter-spacing:-1px;line-height:1}
.hero-title .country{position:absolute;right:0;top:45px;font-family:var(--serif);font-size:32px;line-height:1}

/* location bar */
.locations{left:0;top:439px;width:1102px;height:34px}
.loc-label{position:absolute;font-family:var(--cond);font-size:12px;color:#fff;top:11px}
.loc-label.choose{left:208px;color:#222;font-weight:700}
.loc-icon{position:absolute;top:9px;width:18px;height:16px;border-radius:3px}

/* thumbnails */
.thumb{top:479px;width:161px;height:139px;border:1px solid #ddd;background:#fff;box-shadow:0 2px 3px rgba(0,0,0,.06)}
.thumb .photo{position:absolute;left:7px;top:8px;width:146px;height:107px}
.thumb p{position:absolute;left:8px;top:122px;font-size:8px;color:#444}
.thumb .play{position:absolute;right:11px;top:120px;width:15px;height:14px;background:var(--blue);border-radius:2px}

/* who / deals */
.who{left:207px;top:641px;width:414px}
.section-title{font-family:var(--cond);font-weight:700;letter-spacing:-1.5px}
.who h2{font-size:32px;color:var(--blue);line-height:1}
.who p{font-size:8px;line-height:13.8px;color:#444;margin-top:13px}
.btn{display:inline-block;background:var(--yellow);font-size:8px;color:#333;padding:4px 7px;border-bottom:2px solid #e0a800}
.who .btn{margin-top:11px}
.deals{left:635px;top:641px;width:256px}
.deals-head{height:37px;background:var(--yellow);border-left:7px solid var(--blue);clip-path:polygon(0 0,93% 0,100% 50%,93% 100%,0 100%)}
.deals-head h2{font-size:32px;color:#111;padding-left:17px;line-height:37px}
.deals table{width:250px;border-collapse:collapse;margin:4px 0 0 24px;width:228px}
.deals td{font-size:8px;color:#444;height:18.2px;border-bottom:1px solid var(--line)}
.deals td.price{text-align:right;color:var(--blue)}
.deals .btn{margin:10px 0 0 24px}
.deals-rule{left:635px;top:680px;width:1px;height:140px;background:var(--line)}

/* grey band */
.lower{left:0;top:837px;width:1102px;height:244px;background:linear-gradient(#e5e5e3,#f4f4f2);border-top:1px dotted #ccc}
.fb-box{left:207px;top:860px;width:206px;height:208px;border:1px solid #9aabc8;background:#fff}
.fb-box .bar{height:21px;background:#eef1f7;border-bottom:1px solid #c5cde0;font-size:9px;font-weight:700;color:#333;padding:6px 7px}
.fb-box .page-name{position:absolute;left:43px;top:33px;font-size:9px;font-weight:700;color:var(--blue)}
.fb-box .page-name small{font-weight:400;font-size:7px}
.fb-box .mark{position:absolute;left:8px;top:36px;width:26px;height:20px;background:#e6eef6}
.fb-box .like{position:absolute;left:43px;top:47px;font-size:7px;color:#3b5998;border:1px solid #aab;padding:2px 5px;background:#f2f2f2}
.fb-box .count{position:absolute;left:8px;top:73px;font-size:7.5px;color:#333;border-top:1px solid #ddd;width:190px;padding-top:4px}
.fans{position:absolute;left:8px;top:88px;display:grid;grid-template-columns:repeat(5,35px);column-gap:3px;row-gap:4px}
.fan .pic{width:35px;height:35px}
.fan span{display:block;font-size:6px;color:#777;text-align:center;margin-top:2px}
.fb-box .plugin{position:absolute;left:6px;bottom:4px;font-size:6.5px;color:#777;display:flex;gap:4px;align-items:center}
.fb-box .plugin i{width:8px;height:8px;background:#3b5998;display:inline-block}
.col-rule{top:860px;width:1px;height:200px;background:#d5d5d5}
.lower h3{font-family:var(--cond);font-weight:700;font-size:17px;letter-spacing:-1px;color:#222}
.members{left:433px;top:858px}
.badge{left:447px;top:898px;width:139px;height:127px;background:#fff}
.badge .shape{position:absolute;left:28px;top:22px;width:83px;height:83px;border-radius:50%;background:#dbe7f2}
.news{left:659px;top:858px;width:233px}
.news-item{position:absolute;left:659px;width:233px;height:44px;border-bottom:1px solid #d6d6d6}
.news-item .date{position:absolute;left:1px;top:0;width:29px;height:30px;background:#222;color:#fff;font-family:var(--cond);text-align:center;font-size:12px;line-height:11px;padding-top:3px}
.news-item .date small{display:block;font-size:8px;line-height:9px}
.news-item .date:after{content:"";position:absolute;left:10px;bottom:-5px;border:5px solid transparent;border-top-color:#222;border-bottom:0}
.news-item h4{position:absolute;left:39px;top:0;font-size:8.5px;color:var(--blue);font-weight:700}
.news-item p{position:absolute;left:39px;top:11px;font-size:8px;line-height:10.5px;color:#444;width:190px}
.news-btn{left:659px;top:1049px}

/* footer */
.rule-yellow{left:0;top:1081px;width:1102px;height:5px;background:var(--yellow)}
.site-footer{left:0;top:1086px;width:1102px;height:114px;background:var(--navy)}
.contact{left:208px;top:1108px;color:#fff}
.contact h3{font-family:var(--cond);font-weight:700;font-size:13px;color:var(--yellow);letter-spacing:-.3px}
.contact dl{display:grid;grid-template-columns:42px auto;font-size:8px;line-height:11.8px;margin-top:7px}
.contact dd.mail{color:var(--yellow)}
.follow{left:430px;top:1165px;display:flex;gap:5px;align-items:center;font-size:7.5px;color:#fff}
.follow i{width:11px;height:11px;border-radius:50%;background:var(--yellow);display:inline-block}
.foot-brand{left:603px;top:1113px;font-size:17px;letter-spacing:1.5px;color:#fff}
.foot-brand small{display:block;text-align:right;font-size:5.5px;letter-spacing:2px}
.legal{left:603px;top:1159px;font-size:7.5px;line-height:11px;color:#cfe0ef}
</style>
</head>
<body>
<div class="page">

  <header class="site-header abs">
    <div class="brand abs">VOYAGE HARBOUR<span class="sub">AUSTRALIA</span></div>
    <div class="search abs"><span>Enter Your Keywords Here!</span>
      <div class="go"><svg width="12" height="12" viewBox="0 0 12 12"><circle cx="5" cy="5" r="3.6" fill="none" stroke="#fff" stroke-width="1.6"/><line x1="7.6" y1="7.6" x2="11" y2="11" stroke="#fff" stroke-width="1.8"/></svg></div>
    </div>
    <div class="call abs">
      <svg width="13" height="13" viewBox="0 0 14 14"><path d="M3 1l3 3-1.5 1.5c.8 1.8 2.2 3.2 4 4L10 8l3 3-2 2C6 12.5 1.5 8 1 3z" fill="#2a8fd0"/></svg>
      <span class="label">Call Us Now!</span><span class="num">(02) 5550 1234</span>
    </div>
  </header>

  <nav class="main-nav abs">
    <ul><li>HOME</li><li>AIRFARES</li><li>HOTELS</li><li>CARS</li><li>HOLIDAYS</li><li>CRUISES</li><li>INSURANCE</li><li>CONTACT US</li></ul>
  </nav>
  <div class="newsletter abs"><span>Signup to our Newsletter</span></div>

  <section class="hero abs" role="img" aria-label="Illustration of world landmarks on a globe under a blue sky with planes and balloons"></section>
  <h1 class="hero-title abs"><span class="welcome">WELCOME TO</span><span class="name">VOYAGE HARBOUR</span><span class="country">AUSTRALIA</span></h1>

  <div class="locations abs">
    <svg width="1102" height="34" viewBox="0 0 1102 34" style="position:absolute;left:0;top:0">
      <rect width="1102" height="34" fill="#fcc40f"/>
      <polygon points="386,0 880,0 896,17 880,34 386,34 402,17" fill="#1d5a8e"/>
      <polyline points="492,0 508,17 492,34" fill="none" stroke="#174a76" stroke-width="3"/>
      <polyline points="616,0 632,17 616,34" fill="none" stroke="#174a76" stroke-width="3"/>
      <polyline points="760,0 776,17 760,34" fill="none" stroke="#174a76" stroke-width="3"/>
    </svg>
    <span class="loc-label choose">CHOOSE YOUR LOCATION</span>
    <span class="loc-icon" style="left:348px;background:#f3d77a;border-radius:50%" role="img" aria-label="Globe icon"></span>
    <span class="loc-label" style="left:419px">FLIGHT</span>
    <svg class="loc-icon" style="left:464px" viewBox="0 0 18 16"><path d="M2 9l5-1 4-6h2l-2 6 5-1 1-2h1l-1 4 1 4h-1l-1-2-5-1 2 6h-2l-4-6-5-1z" fill="#dfe8f1"/></svg>
    <span class="loc-label" style="left:529px">COACH</span>
    <span class="loc-icon" style="left:572px;width:32px;background:#c9d3dd" role="img" aria-label="Coach icon"></span>
    <span class="loc-label" style="left:660px">ADVENTURE</span>
    <span class="loc-icon" style="left:730px;width:24px;background:#c79a63" role="img" aria-label="Mountain icon"></span>
    <span class="loc-label" style="left:797px">CRUISE</span>
    <span class="loc-icon" style="left:844px;width:26px;background:#e06b5a" role="img" aria-label="Cruise ship icon"></span>
  </div>

  <article class="thumb abs" style="left:207px"><div class="photo" role="img" aria-label="Resort villa with pool" style="background:linear-gradient(#6a8f4a,#8a4a3a 60%,#3aa0c0)"></div><p>Lorem ipsum dolor sit amet.</p><span class="play"></span></article>
  <article class="thumb abs" style="left:379px"><div class="photo" role="img" aria-label="Palm trees by a hotel pool" style="background:linear-gradient(#2f7fd0,#8cc0e0 55%,#2bb0c8)"></div><p>Lorem ipsum dolor sit amet.</p><span class="play"></span></article>
  <article class="thumb abs" style="left:553px"><div class="photo" role="img" aria-label="Harbour city skyline at dusk" style="background:linear-gradient(#0b3fa8,#2d6fd0 70%,#c9d4e8)"></div><p>Lorem ipsum dolor sit amet.</p><span class="play"></span></article>
  <article class="thumb abs" style="left:729px"><div class="photo" role="img" aria-label="Cruise ship docked at harbour" style="background:linear-gradient(#4f8ed6,#dfe6ee 60%,#315a80)"></div><p>Lorem ipsum dolor sit amet.</p><span class="play"></span></article>

  <section class="who abs">
    <h2 class="section-title">WHO WE ARE?</h2>
    <p>Lorem ipsum dolor sit amet, consectetur adipisicing elit, sed do eiusmod tempor incididunt ut labore et dolore magna aliqua. Ut enim ad minim veniam, quis nostrud exercitation ullamco laboris nisi ut aliquip ex ea commodo consequat. Duis aute irure dolor in reprehenderit in voluptate velit esse cillum dolore eu fugiat nulla pariatur. Excepteur sint occaecat cupidatat non proident, sunt in culpa qui officia deserunt mollit anim id est laborum.</p>
    <p>Sed ut perspiciatis unde omnis iste natus error sit voluptatem accusantium doloremque laudantium, totam rem aperiam..</p>
    <span class="btn">View Details</span>
  </section>

  <div class="deals-rule abs"></div>
  <section class="deals abs">
    <div class="deals-head"><h2 class="section-title">HOT DEALS</h2></div>
    <table>
      <tr><td>Alexandria Extension</td><td class="price">$235*</td></tr>
      <tr><td>3 Night Whitsundays Hotel</td><td class="price">$480*</td></tr>
      <tr><td>7 Day Ireland Tour</td><td class="price">$1,189*</td></tr>
      <tr><td>9 Day Spanish Guided Holiday</td><td class="price">$1,620*</td></tr>
      <tr><td>8 Day Britain &amp; Ireland Tour</td><td class="price">$1,749*</td></tr>
      <tr><td>23 Day Central America Tour</td><td class="price">$3,598*</td></tr>
    </table>
    <span class="btn">View Details</span>
  </section>

  <section class="lower abs"></section>

  <aside class="fb-box abs">
    <div class="bar">Find us on Friendbook</div>
    <span class="mark"></span>
    <div class="page-name">Voyage Harbour <small>on Friendbook</small></div>
    <span class="like">Like</span>
    <div class="count">618 people like <b>Voyage Harbour</b>.</div>
    <div class="fans">
      <div class="fan"><div class="pic" role="img" aria-label="Fan photo" style="background:#b07a5a"></div><span>Tara</span></div>
      <div class="fan"><div class="pic" role="img" aria-label="Fan photo" style="background:#c98a6a"></div><span>Mina</span></div>
      <div class="fan"><div class="pic" role="img" aria-label="Fan photo" style="background:#8a9aa8"></div><span>Sam</span></div>
      <div class="fan"><div class="pic" role="img" aria-label="Fan photo" style="background:#6f8a5a"></div><span>Dana</span></div>
      <div class="fan"><div class="pic" role="img" aria-label="Fan photo" style="background:#a89a8a"></div><span>Aled</span></div>
      <div class="fan"><div class="pic" role="img" aria-label="Fan photo" style="background:#c9a08a"></div><span>Cris</span></div>
      <div class="fan"><div class="pic" role="img" aria-label="Fan photo" style="background:#b8865e"></div><span>Ana Rosa</span></div>
      <div class="fan"><div class="pic" role="img" aria-label="Fan photo" style="background:#4a4a4a"></div><span>Abe</span></div>
      <div class="fan"><div class="pic" role="img" aria-label="Fan photo" style="background:#6a4a5a"></div><span>Alia</span></div>
      <div class="fan"><div class="pic" role="img" aria-label="Fan photo" style="background:#1e1e1e"></div><span>Cole</span></div>
    </div>
    <div class="plugin"><i></i>Friendbook social plugin</div>
  </aside>

  <div class="col-rule abs" style="left:419px"></div>
  <h3 class="members abs">WE ARE MEMBER OF</h3>
  <div class="badge abs" role="img" aria-label="Travel association membership badge"><span class="shape"></span></div>

  <div class="col-rule abs" style="left:635px"></div>
  <h3 class="news abs">LATEST NEWS</h3>
  <div class="news-item abs" style="top:898px"><div class="date">12<small>DEC</small></div><h4>Lorem ipsum dolor sit amet,</h4><p>consectetuer adipiscing elit, sed diam nonummy nibh euismod tincidunt ut laoreet dolore magna</p></div>
  <div class="news-item abs" style="top:947px"><div class="date">12<small>DEC</small></div><h4>Lorem ipsum dolor sit amet,</h4><p>consectetuer adipiscing elit, sed diam nonummy nibh euismod tincidunt ut laoreet dolore magna</p></div>
  <div class="news-item abs" style="top:1000px;border:none"><div class="date">11<small>DEC</small></div><h4>Lorem ipsum dolor sit amet,</h4><p>consectetuer adipiscing elit, sed diam nonummy nibh euismod tincidunt ut laoreet dolore magna</p></div>
  <span class="btn news-btn abs">View Details</span>

  <div class="rule-yellow abs"></div>
  <footer class="site-footer abs"></footer>
  <div class="contact abs">
    <h3>CONTACT US</h3>
    <dl>
      <dt>Address:</dt><dd>P.O Box 120 Harbourside NSW 2000</dd>
      <dt>Phone:</dt><dd>(+612) 5550 1234</dd>
      <dt>Fax:</dt><dd>(+612) 555 012 34</dd>
      <dt>E-mail:</dt><dd class="mail">sales@voyageharbour-example.com.au</dd>
    </dl>
  </div>
  <div class="follow abs">Follow us on :<i></i><i></i><i></i><i></i><i></i></div>
  <div class="foot-brand abs">VOYAGE HARBOUR<small>AUSTRALIA</small></div>
  <p class="legal abs">2005 - 2009 Voyage Harbour PTY LTD. All Rights Reserved.<br>Lic.2TA 0000. Participant of the Traveller Protection Fund file number 0000</p>

</div>
</body>
</html>
```